Green Energy Conservation Business Cards

We believe in Conserve before you produce energy. I am looking for a unique, bold business card. that Demonstrates Expertise in our field. I would be interested to try and incorporate a night picture of the US or world showing the yellow lights on one side. I would be open to a design that caters to half the business card size height and same length. Our primary expertise is Energy projects for self storage. Use either black or white background .Attached are the logos and symbols.

May I see some design utilizing a smaller business card. the same length as a normal business card but cut in half on the height. best regards Garvel

```html
<!DOCTYPE html>
<html lang="en">
<head>
<meta charset="utf-8">
<title>Verdo Energy Group – Business Cards</title>
<link href="https://fonts.googleapis.com/css2?family=Open+Sans:wght@300;400;600&display=swap" rel="stylesheet">
<style>
  :root {
    --backdrop: #e8e5e0;
    --card-black: #050505;
    --corner-white: #ffffff;
    --text-white: #f2f2f2;
    --brand-green: #7cc242;
    --city-gold: #e8b21c;
    --city-amber: #a86a08;
    --city-dark: #2a1a04;
  }
  * { margin: 0; padding: 0; box-sizing: border-box; }
  html, body {
    width: 1200px;
    height: 805px;
    overflow: hidden;
    background: var(--backdrop);
    font-family: "Open Sans", Arial, sans-serif;
  }
  .sheet {
    position: relative;
    width: 1200px;
    height: 805px;
    display: flex;
    flex-direction: column;
    align-items: center;
    justify-content: center;
    gap: 44px;
  }
  .card {
    position: relative;
    width: 620px;
    height: 354px;
    background: var(--card-black);
    overflow: hidden;
    box-shadow: 0 6px 18px rgba(0,0,0,0.18);
  }

  /* Front */
  .card-front .city-lights {
    position: absolute;
    left: 0; top: 0;
    width: 64%;
    height: 100%;
    background:
      radial-gradient(ellipse 60% 90% at 100% 50%, rgba(255,226,120,0.85) 0%, rgba(232,178,28,0.55) 30%, transparent 70%),
      linear-gradient(90deg, var(--city-dark) 0%, var(--city-amber) 45%, var(--city-gold) 80%, rgba(5,5,5,0) 100%);
  }
  .card-front .city-fade {
    position: absolute;
    left: 52%; top: 0;
    width: 20%;
    height: 100%;
    background: linear-gradient(90deg, rgba(5,5,5,0) 0%, var(--card-black) 100%);
  }
  .brand {
    position: absolute;
    display: flex;
    align-items: center;
    gap: 12px;
  }
  .brand-dot {
    width: 40px;
    height: 40px;
    border-radius: 50%;
    background: var(--brand-green);
    flex: none;
  }
  .brand-name {
    color: var(--brand-green);
    font-weight: 600;
    font-size: 24px;
    line-height: 1.1;
  }
  .card-front .brand { right: 30px; top: 50%; transform: translateY(-50%); }

  /* Back */
  .corner {
    position: absolute;
    width: 0; height: 0;
  }
  .corner-top {
    top: 0; left: 0;
    border-top: 120px solid var(--corner-white);
    border-right: 150px solid transparent;
  }
  .corner-bottom {
    bottom: 0; right: 0;
    border-bottom: 120px solid var(--corner-white);
    border-left: 150px solid transparent;
  }
  .card-back .brand { right: 42px; top: 44px; }
  .contact {
    position: absolute;
    left: 64px;
    top: 134px;
    color: var(--text-white);
  }
  .contact-name {
    font-weight: 300;
    font-size: 24px;
    letter-spacing: 0.5px;
    text-transform: uppercase;
  }
  .contact-title {
    font-weight: 300;
    font-size: 15px;
    margin-top: 2px;
  }
  .contact-rule {
    width: 220px;
    height: 1px;
    background: var(--text-white);
    margin: 16px 0 14px;
  }
  .contact-list {
    list-style: none;
    font-size: 13px;
    line-height: 1.55;
  }
</style>
</head>
<body>
<main class="sheet">
  <section class="card card-front" aria-label="Business card front">
    <div class="city-lights" role="img" aria-label="Night aerial view of a city glowing with yellow lights"></div>
    <div class="city-fade"></div>
    <div class="brand">
      <span class="brand-dot"></span>
      <span class="brand-name">Verdo<br>Energy Group</span>
    </div>
  </section>

  <section class="card card-back" aria-label="Business card back">
    <div class="corner corner-top"></div>
    <div class="corner corner-bottom"></div>
    <div class="brand">
      <span class="brand-dot"></span>
      <span class="brand-name">Verdo<br>Energy Group</span>
    </div>
    <div class="contact">
      <p class="contact-name">Dustin Garvel</p>
      <p class="contact-title">President</p>
      <div class="contact-rule"></div>
      <ul class="contact-list">
        <li>Phone: 555-010-2288</li>
        <li>Email: dustin@verdoenergy.com</li>
        <li>Website: www.verdoenergy.com</li>
        <li>Address: 48 Harbor Lane, Norfolk, VA 23510</li>
      </ul>
    </div>
  </section>
</main>
</body>
</html>
```